Professional BBQ Cleaning Flyer (Before & After Focus)

We need a clean, professional double-sided A5 flyer for a BBQ cleaning business.
This flyer will be handed directly to:
Property managers
Retirement villages
Over 50s communities
Resorts / body corporate
The design must feel professional, trustworthy, and easy to read β not cluttered or cheap.
π― Goal
Use a strong before & after BBQ image to show the value of the service, and position the business as reliable for communal BBQ cleaning.
π Size & Format
A5 (148 x 210mm)
Portrait (vertical)
Double-sided
Print-ready (with bleed)
π¨ Style & Branding
Colours: Red, Black, White
Clean, modern, minimal
Strong, easy-to-read fonts (important for older audience)
Plenty of white space
No emojis, no clutter, no cheap design elements
π₯ FRONT SIDE (IMPORTANT β MAIN FOCUS)
Must include:
Headline:
Professional BBQ Cleaning
For Shared & Communal Areas
Subheadline:
Keep your BBQs clean, safe, and ready for residents & guests
Main Visual :
Side-by-side BEFORE & AFTER BBQ
This is the main focus of the flyer
Must be realistic and high quality
Labels under images:
BEFORE β Greasy β’ Dirty β’ Unsafe
AFTER β Clean β’ Hygienic β’ Ready to Use
Short Bullet Points:
Deep clean of grills, burners & internal components
Ideal for retirement villages, resorts & body corporate
Multiple BBQs cleaned in one visit
Trust Line:
Fully insured & police checked
Call to Action (bottom):
Get a Quote or Book a Service
0438 254 091
www.grillshinecrew.com.au
β¬ BACK SIDE (CREDIBILITY & DETAIL)
Headline:
Trusted by Property Managers & Facilities Teams
Whatβs Included:
Full dismantle and deep clean
Removal of grease, carbon & built-up residue
Grills, burners, trays & surfaces cleaned
Reassembled and checked
Why Choose Us:
Professional, reliable service
Works around your schedule
Ideal for high-use communal BBQ areas
One-off or ongoing maintenance
Ideal For:
Retirement villages
Apartment complexes
Resorts
Body corporate properties
Closing Line:
Keep your shared BBQ areas clean, safe, and presentable year-round
Contact:
Grill Shine Crew
0438 254 091
www.grillshinecrew.com.au
grillshinecrew@mailbox-demo.com.au

```html
<!DOCTYPE html>
<html lang="en">
<head>
<meta charset="utf-8">
<title>Grill Shine Crew – BBQ Cleaning Flyer</title>
<link href="https://fonts.googleapis.com/css2?family=Poppins:wght@400;500;600;700;800&display=swap" rel="stylesheet">
<style>
:root{
  --red:#e8203a;
  --red-dark:#c8172d;
  --black:#111111;
  --white:#ffffff;
  --ink:#1a1a1a;
  --stage:#d6d6d6;
}
*{box-sizing:border-box;margin:0;padding:0}
html,body{width:1200px;height:804px;overflow:hidden}
body{background:var(--stage);font-family:"Poppins",sans-serif;color:var(--ink);position:relative}
.flyer{position:absolute;top:118px;width:386px;height:548px;background:var(--white);overflow:hidden}
.flyer--front{left:164px}
.flyer--back{left:666px}
.abs{position:absolute}

/* brand */
.brand{display:flex;align-items:center;gap:6px}
.brand__dot{width:22px;height:22px;border-radius:50%;background:var(--red)}
.brand__name{font-weight:700;color:var(--black);font-size:15px;line-height:1}

/* front */
.front-brand{top:30px;left:0;width:100%;justify-content:center}
.front-eyebrow{top:80px;width:100%;text-align:center;font-weight:600;font-size:13px;letter-spacing:3px;color:var(--black)}
.front-title{top:96px;width:100%;text-align:center;font-weight:800;font-size:32px;color:var(--red);line-height:1.1}
.front-sub{top:135px;width:100%;text-align:center;font-weight:700;font-size:10.5px;color:var(--black)}
.front-lede{top:155px;width:100%;text-align:center;font-weight:600;font-size:13px;color:var(--black);line-height:1.25}
.front-band{top:264px;left:0;width:100%;height:244px;background:var(--black)}
.compare{top:190px;left:25px;width:336px;height:184px;display:flex;gap:3px;background:var(--red)}
.compare__side{position:relative;flex:1;display:flex;flex-direction:column}
.compare__photo{flex:1}
.compare__photo--before{background:linear-gradient(160deg,#5b5650,#2b2824 60%,#4a4540)}
.compare__photo--after{background:linear-gradient(160deg,#d7d9db,#9da2a6 55%,#c9ccce)}
.compare__tag{position:absolute;top:0;left:0;padding:4px 14px;font-weight:800;font-size:15px;color:var(--white)}
.compare__tag--before{background:var(--black)}
.compare__tag--after{background:var(--red)}
.compare__labels{height:42px;display:flex;align-items:center;justify-content:space-around;background:var(--red)}
.compare__side:last-child .compare__labels{background:var(--red-dark)}
.compare__label{display:flex;flex-direction:column;align-items:center;gap:2px;font-weight:700;font-size:9.5px;color:var(--white)}
.compare__label svg{width:9px;height:9px}
.front-points{top:392px;left:26px;width:226px;list-style:none}
.front-points li,.tick-list li{position:relative;padding-left:12px;font-weight:600;font-size:9px;line-height:1.25;color:var(--white);margin-bottom:5px}
.front-points li::before,.tick-list li::before{content:"";position:absolute;left:0;top:3px;width:6px;height:6px;border-radius:50%;background:var(--red)}
.trust-badge{top:384px;left:250px;width:82px;height:82px}
.trust-badge__text{position:absolute;inset:0;display:flex;align-items:center;justify-content:center;text-align:center;font-weight:800;font-size:7.5px;line-height:1.2;color:var(--white)}
.cta{top:474px;left:28px;width:330px;height:30px;border-radius:15px;background:var(--red);display:flex;align-items:center;justify-content:space-between;padding:0 8px 0 10px}
.cta__text{font-weight:600;font-size:12.5px;color:var(--white)}
.cta__phone{display:flex;align-items:center;gap:6px;font-weight:700;font-size:13px;color:var(--white)}
.cta__icon{width:22px;height:22px;border-radius:50%;background:var(--black);display:flex;align-items:center;justify-content:center}
.front-url{top:516px;width:100%;text-align:center;font-weight:700;font-size:14.5px;color:var(--black)}

/* back */
.back-eyebrow{top:24px;width:100%;text-align:center;font-weight:700;font-size:16px;letter-spacing:2px;color:var(--black)}
.back-title{top:42px;width:100%;text-align:center;font-weight:800;font-size:21px;line-height:1.12;color:var(--red)}
.back-title span{display:block;color:var(--black)}
.back-band{top:104px;left:0;width:100%;height:164px;background:var(--black)}
.back-photo{top:128px;left:26px;width:138px;height:118px;background:linear-gradient(135deg,#c9b49a,#8a7f6c 50%,#e8d3a8)}
.included{top:124px;left:180px;width:196px}
.section-head{font-weight:700;font-size:15px;line-height:1.2}
.included .section-head{color:var(--red);margin-bottom:8px}
.tick-list{list-style:none}
.included .tick-list li{font-size:8.5px;margin-bottom:9px}
.why{top:268px;left:26px;width:203px;height:158px;background:var(--red);border-radius:0 0 4px 4px;padding:14px 12px}
.why .section-head{color:var(--black);margin-bottom:8px}
.why .tick-list li{font-size:8.5px;margin-bottom:6px}
.why .tick-list li::before{background:var(--white)}
.ideal{top:286px;left:253px;width:120px}
.ideal .section-head{color:var(--red);margin-bottom:8px}
.ideal__list{list-style:none}
.ideal__item{display:flex;align-items:center;gap:8px;font-weight:600;font-size:8.5px;line-height:1.2;color:var(--black);margin-bottom:10px}
.ideal__item svg{width:15px;height:15px;flex:none}
.closing{top:442px;width:100%;text-align:center;font-weight:800;font-size:13.5px;line-height:1.25;color:var(--black)}
.closing span{display:block;color:var(--red)}
.back-brand{top:486px;left:22px}
.back-brand .brand__name{font-size:11px;width:60px;line-height:1.1}
.contact-bar{top:484px;left:132px;width:256px;height:19px;background:var(--black);border-radius:10px 0 0 10px;display:flex;align-items:center;gap:8px;padding-left:10px}
.contact-bar__item{display:flex;align-items:center;gap:4px;font-size:7.5px;font-weight:500;color:var(--white);white-space:nowrap}
.contact-bar__icon{width:9px;height:9px;border-radius:50%;background:var(--red);display:flex;align-items:center;justify-content:center}
.back-url{top:506px;left:132px;width:240px;text-align:center;font-weight:700;font-size:14px;color:var(--black)}
</style>
</head>
<body>

<section class="flyer flyer--front">
  <div class="abs brand front-brand"><span class="brand__dot"></span><span class="brand__name">Grill Shine Crew</span></div>
  <p class="abs front-eyebrow">PROFESSIONAL</p>
  <h1 class="abs front-title">BBQ CLEANING</h1>
  <p class="abs front-sub">FOR SHARED &amp; COMMUNAL AREAS</p>
  <p class="abs front-lede">Keep your BBQs clean,<br>safe, and ready for residents &amp; guests</p>

  <div class="abs front-band"></div>
  <div class="abs compare">
    <div class="compare__side">
      <div class="compare__photo compare__photo--before" role="img" aria-label="Dirty, greasy BBQ grill before cleaning"></div>
      <span class="compare__tag compare__tag--before">BEFORE</span>
      <div class="compare__labels">
        <span class="compare__label"><svg viewBox="0 0 10 10"><circle cx="5" cy="5" r="5" fill="#111"/></svg>Greasy</span>
        <span class="compare__label"><svg viewBox="0 0 10 10"><circle cx="5" cy="5" r="5" fill="#111"/></svg>Dirty</span>
        <span class="compare__label"><svg viewBox="0 0 10 10"><circle cx="5" cy="5" r="5" fill="#111"/></svg>Unsafe</span>
      </div>
    </div>
    <div class="compare__side">
      <div class="compare__photo compare__photo--after" role="img" aria-label="Shiny stainless BBQ grill after cleaning"></div>
      <span class="compare__tag compare__tag--after">AFTER</span>
      <div class="compare__labels">
        <span class="compare__label"><svg viewBox="0 0 10 10"><circle cx="5" cy="5" r="5" fill="#111"/><path d="M2.8 5.2l1.5 1.5 3-3" stroke="#fff" stroke-width="1.2" fill="none"/></svg>Clean</span>
        <span class="compare__label"><svg viewBox="0 0 10 10"><circle cx="5" cy="5" r="5" fill="#111"/><path d="M2.8 5.2l1.5 1.5 3-3" stroke="#fff" stroke-width="1.2" fill="none"/></svg>Hygienic</span>
        <span class="compare__label"><svg viewBox="0 0 10 10"><circle cx="5" cy="5" r="5" fill="#111"/><path d="M2.8 5.2l1.5 1.5 3-3" stroke="#fff" stroke-width="1.2" fill="none"/></svg>Ready to Use</span>
      </div>
    </div>
  </div>

  <ul class="abs front-points">
    <li>Deep clean of grills, burners &amp; internal components</li>
    <li>Ideal for retirement villages, resorts &amp; body corporate</li>
    <li>Multiple BBQs cleaned in one visit</li>
  </ul>
  <div class="abs trust-badge">
    <svg viewBox="0 0 100 100" width="82" height="82"><polygon fill="#e8203a" points="50,0 57,13 70,4 72,19 87,13 84,28 99,28 91,41 100,50 91,59 99,72 84,72 87,87 72,81 70,96 57,87 50,100 43,87 30,96 28,81 13,87 16,72 1,72 9,59 0,50 9,41 1,28 16,28 13,13 28,19 30,4 43,13"/></svg>
    <span class="trust-badge__text">FULLY<br>INSURED &amp;<br>POLICE<br>CHECKED</span>
  </div>

  <div class="abs cta">
    <span class="cta__text">Get a Quote or Book a Service</span>
    <span class="cta__phone"><span class="cta__icon"><svg viewBox="0 0 24 24" width="12" height="12"><path fill="#fff" d="M6.6 10.8a15 15 0 006.6 6.6l2.2-2.2a1 1 0 011-.25 11.4 11.4 0 003.6.57 1 1 0 011 1V20a1 1 0 01-1 1A17 17 0 013 4a1 1 0 011-1h3.5a1 1 0 011 1c0 1.25.2 2.45.57 3.57a1 1 0 01-.25 1z"/></svg></span>0438 254 091</span>
  </div>
  <p class="abs front-url">www.grillshinecrew.com.au</p>
</section>

<section class="flyer flyer--back">
  <p class="abs back-eyebrow">TRUSTED BY</p>
  <h2 class="abs back-title">PROPERTY MANAGERS &amp;<span>FACILITIES TEAMS</span></h2>

  <div class="abs back-band"></div>
  <div class="abs back-photo" role="img" aria-label="Family enjoying a barbecue outdoors"></div>
  <div class="abs included">
    <h3 class="section-head">What’s Included</h3>
    <ul class="tick-list">
      <li>Full dismantle and deep clean</li>
      <li>Removal of grease, carbon &amp;<br>built-up residue</li>
      <li>Grills, burners, trays &amp; surfaces<br>cleaned</li>
      <li>Reassembled and checked</li>
    </ul>
  </div>

  <div class="abs why">
    <h3 class="section-head">Why Choose Us</h3>
    <ul class="tick-list">
      <li>Professional, reliable service</li>
      <li>Works around your schedule</li>
      <li>Ideal for high-use communal BBQ areas</li>
      <li>One-off or ongoing maintenance</li>
      <li>Fully insured &amp; police checked</li>
    </ul>
  </div>

  <div class="abs ideal">
    <h3 class="section-head">IDEAL FOR</h3>
    <ul class="ideal__list">
      <li class="ideal__item"><svg viewBox="0 0 16 16"><path fill="#e8203a" d="M1 15V7l7-5 7 5v8H10v-4H6v4z"/></svg>Retirement villages</li>
      <li class="ideal__item"><svg viewBox="0 0 16 16"><path fill="#e8203a" d="M2 15V3h7v12zm8 0V7h4v8z"/></svg>Apartment complexes</li>
      <li class="ideal__item"><svg viewBox="0 0 16 16"><path fill="#e8203a" d="M1 15V6l7-4 7 4v9z"/></svg>Resorts</li>
      <li class="ideal__item"><svg viewBox="0 0 16 16"><path fill="#e8203a" d="M2 15V5h5V1h7v14z"/></svg>Body corporate properties</li>
    </ul>
  </div>

  <p class="abs closing">KEEP YOUR SHARED BBQ AREAS CLEAN, SAFE,<span>&amp; PRESENTABLE YEAR-ROUND</span></p>

  <div class="abs brand back-brand"><span class="brand__dot"></span><span class="brand__name">Grill Shine Crew</span></div>
  <div class="abs contact-bar">
    <span class="contact-bar__item"><span class="contact-bar__icon"><svg viewBox="0 0 24 24" width="6" height="6"><path fill="#fff" d="M6.6 10.8a15 15 0 006.6 6.6l2.2-2.2a1 1 0 011-.25 11.4 11.4 0 003.6.57 1 1 0 011 1V20a1 1 0 01-1 1A17 17 0 013 4a1 1 0 011-1h3.5a1 1 0 011 1c0 1.25.2 2.45.57 3.57a1 1 0 01-.25 1z"/></svg></span>0438 254 091</span>
    <span class="contact-bar__item"><span class="contact-bar__icon"><svg viewBox="0 0 24 24" width="6" height="6"><path fill="#fff" d="M2 5h20v14H2zm2 2v.5l8 5 8-5V7z"/></svg></span>grillshinecrew@mailbox-demo.com.au</span>
  </div>
  <p class="abs back-url">www.grillshinecrew.com.au</p>
</section>

</body>
</html>
```